Lumorva presentation

We built A 20-page powerpoint document. We would like to change the look of this document. We work in digital area. So, we would like something more modern, more current and less classical. We need to be fashionable while remaining reassuring for corporate. Our business is to make recommendations in 5 days where our competitors do it in 3 months.

Target Market(s)

medium sized business, or a large global enterprise

Industry/Entity Type

Digital

Colors

Designer to choose colors to be used in the design.

Requirements
Must have
• We are working with digital expert. We need to surprise them.

```html
<!DOCTYPE html>
<html lang="fr">
<head>
<meta charset="utf-8">
<title>Lumorva – 360° Digital Sprint Assessment</title>
<link href="https://fonts.googleapis.com/css2?family=Raleway:wght@300;400;500;600&display=swap" rel="stylesheet">
<style>
  :root{
    --page:#ffffff;
    --slide-bg:#1b1b1d;
    --slide-edge:#2a2a2e;
    --blue:#1f6fc4;
    --blue-bright:#3a8ee6;
    --blue-deep:#103c6e;
    --text:#ffffff;
    --text-soft:#d9dde3;
    --link:#5aa6f0;
  }
  *{margin:0;padding:0;box-sizing:border-box}
  html,body{width:1200px;height:946px;overflow:hidden;background:var(--page)}
  body{position:relative;font-family:"Raleway",Arial,sans-serif;color:var(--text)}
  .slide{position:absolute;width:556px;height:311px;background:var(--slide-bg);overflow:hidden;border:1px solid var(--slide-edge)}
  .col-a{left:21px}.col-b{left:620px}
  .row-1{top:2px}.row-2{top:316px}.row-3{top:631px}
  .swoosh{position:absolute;inset:0;width:100%;height:100%}
  .photo{position:absolute;inset:0}
  .photo-beach{background:linear-gradient(120deg,#1d2a33 0%,#22313a 35%,#161c22 70%,#1b1b1d 100%)}
  .photo-bridge{background:linear-gradient(100deg,#1b1b1d 0%,#262b31 40%,#39414a 70%,#2b3036 100%)}
  .emblem{position:absolute;left:20px;top:16px;width:40px;height:42px;background:var(--blue);border-radius:4px;opacity:.85}
  .brand{position:absolute;right:30px;top:42px;display:flex;align-items:center;gap:5px;font-size:13px;font-weight:600;color:var(--text)}
  .brand-dot{width:9px;height:9px;border-radius:50%;background:var(--blue-bright)}
  .cover-title{position:absolute;right:32px;top:150px;text-align:right;font-size:26px;font-weight:300;line-height:1.25}
  .cover-date{position:absolute;right:32px;top:252px;font-size:13px;color:var(--link);font-weight:400}
  .quote-mark{position:absolute;left:53px;top:74px;font-size:48px;color:var(--blue-bright);font-weight:500;line-height:1}
  .quote-text{position:absolute;left:54px;top:106px;font-size:33px;font-weight:400;line-height:38px}
  .slide-title{position:absolute;left:67px;top:30px;font-size:24px;font-weight:400}
  .section-head{position:absolute;left:72px;top:84px;font-size:13px;font-weight:400;display:flex;align-items:center;gap:6px}
  .chev{width:8px;height:8px;border-radius:50%;border:2px solid var(--blue-bright);border-right-color:transparent;flex:none}
  .toc{position:absolute;left:73px;top:68px;list-style:none}
  .toc-part{font-size:13.5px;display:flex;align-items:center;gap:7px;margin-top:6px}
  .toc-part:first-child{margin-top:0}
  .toc-sub{list-style:none;margin:2px 0 0 22px}
  .toc-sub li{font-size:8.6px;color:var(--link);line-height:12.5px}
  .toc-sub li::before{content:"•";margin-right:5px}
  .hex-ring{position:absolute;left:260px;top:60px;width:260px;height:245px}
  .hex-label{fill:var(--text);font-size:7.5px;font-family:"Raleway",Arial,sans-serif;text-anchor:middle}
  .ribbons{position:absolute;left:62px;top:122px;width:345px}
  .ribbon{position:relative;height:34px;margin-bottom:5px;display:flex;align-items:center;padding-left:66px;font-size:8.5px;line-height:10.5px;background:linear-gradient(90deg,var(--blue-deep),var(--blue));border-radius:0 6px 6px 0}
  .ribbon::before{content:"";position:absolute;left:0;top:-5px;width:42px;height:28px;background:var(--blue);clip-path:polygon(0 0,80% 0,100% 30%,100% 100%,0 100%)}
  .deliverables{position:absolute;left:92px;top:114px;width:430px;list-style:none}
  .deliverables li{font-size:10.5px;line-height:12.5px;margin-bottom:3px;padding-left:10px;position:relative;color:var(--text-soft)}
  .deliverables li::before{content:"•";position:absolute;left:0}
</style>
</head>
<body>

<!-- Cover -->
<section class="slide col-a row-1">
  <div class="photo photo-beach" role="img" aria-label="Photo d'une personne courant sur une plage au crépuscule"></div>
  <div class="emblem" role="img" aria-label="Silhouette d'un coureur"></div>
  <div class="brand"><span class="brand-dot"></span>Lumorva</div>
  <h1 class="cover-title">360˚ Digital Sprint<br>Assessment<br>–</h1>
  <p class="cover-date">13 juillet 2017</p>
</section>

<!-- Quote -->
<section class="slide col-b row-1">
  <svg class="swoosh" viewBox="0 0 556 311" preserveAspectRatio="none" aria-hidden="true">
    <defs><linearGradient id="sw1" x1="0" y1="0" x2="1" y2="1"><stop offset="0" stop-color="#0f2f57"/><stop offset="1" stop-color="#1a4f8c"/></linearGradient></defs>
    <path d="M420 0 C520 80 560 200 470 311 L556 311 L556 0 Z" fill="url(#sw1)" opacity=".75"/>
  </svg>
  <div class="emblem" role="img" aria-label="Silhouette d'un coureur"></div>
  <div class="brand"><span class="brand-dot"></span>Lumorva</div>
  <div class="quote-mark">“</div>
  <p class="quote-text">Le déni de voir<br>l’évolution<br>est un délit!</p>
</section>

<!-- Summary -->
<section class="slide col-a row-2">
  <svg class="swoosh" viewBox="0 0 556 311" preserveAspectRatio="none" aria-hidden="true">
    <defs><linearGradient id="sw2" x1="0" y1="0" x2="1" y2="1"><stop offset="0" stop-color="#0f2f57"/><stop offset="1" stop-color="#1a4f8c"/></linearGradient></defs>
    <path d="M400 0 C520 90 560 210 450 311 L556 311 L556 0 Z" fill="url(#sw2)" opacity=".75"/>
  </svg>
  <div class="emblem" role="img" aria-label="Silhouette d'un coureur"></div>
  <div class="brand"><span class="brand-dot"></span>Lumorva</div>
  <h2 class="slide-title">Sommaire</h2>
  <ol class="toc" style="top:72px">
    <li>
      <div class="toc-part"><span class="chev"></span>1. Le sprint c’est quoi ?</div>
      <ul class="toc-sub">
        <li>A. Un concept innovant</li>
        <li>B. Partis-pris: une approche d’expertises interconnectées</li>
        <li>C. Livrables</li>
        <li>D. Experts</li>
      </ul>
    </li>
    <li>
      <div class="toc-part"><span class="chev"></span>2. Process détaillé</div>
      <ul class="toc-sub">
        <li>J-1: Questionnement préalable</li>
        <li>Jour 1 : Vers un enrichissement du questionnement</li>
        <li>Jour 2 : La vision 360°</li>
        <li>Jour 3 : Les leviers de la transformation</li>
        <li>Jour 4 : Transformer la façon dont on doit se transformer</li>
        <li>Jour 5 : On se lance !</li>
        <li>Le jour d’après</li>
      </ul>
    </li>
    <li>
      <div class="toc-part"><span class="chev"></span>3. Références des experts</div>
    </li>
  </ol>
</section>

<!-- Concept -->
<section class="slide col-b row-2">
  <div class="photo photo-bridge" role="img" aria-label="Photo d'une coureuse sur un pont en ville"></div>
  <div class="emblem" role="img" aria-label="Silhouette d'un coureur"></div>
  <div class="brand"><span class="brand-dot"></span>Lumorva</div>
  <h2 class="slide-title">1. Le sprint c’est quoi ?</h2>
  <div class="section-head"><span class="chev"></span>A/ un concept innovant:</div>
  <svg class="hex-ring" viewBox="0 0 260 245" aria-label="Six piliers du sprint">
    <g fill="#1f6fc4" stroke="#1b1b1d" stroke-width="2">
      <polygon points="123,4 158,24 158,64 123,84 88,64 88,24"/>
      <polygon points="181,40 216,60 216,100 181,120 146,100 146,60"/>
      <polygon points="181,118 216,138 216,178 181,198 146,178 146,138"/>
      <polygon points="123,152 158,172 158,212 123,232 88,212 88,172"/>
      <polygon points="61,116 96,136 96,176 61,196 26,176 26,136"/>
      <polygon points="61,40 96,60 96,100 61,120 26,100 26,60"/>
    </g>
    <g fill="none" stroke="#ffffff" stroke-width="1.4">
      <circle cx="123" cy="30" r="6"/>
      <path d="M175 70 h12 M181 66 v14 M175 76 l-3 6 h6 z M187 76 l-3 6 h6 z"/>
      <path d="M173 154 h16 M175 156 v10 M181 156 v10 M187 156 v10 M172 168 h18"/>
      <path d="M123 178 l4 8 v8 h-8 v-8 z"/>
      <circle cx="61" cy="144" r="7"/>
      <path d="M53 72 l8 6 l8 -6"/>
    </g>
    <text class="hex-label" x="123" y="50">Conjugaison</text>
    <text class="hex-label" x="123" y="59">d’expertises</text>
    <text class="hex-label" x="123" y="68">élevées</text>
    <text class="hex-label" x="181" y="96">Regarder</text>
    <text class="hex-label" x="181" y="105">autrement</text>
    <text class="hex-label" x="181" y="182">5 jours</text>
    <text class="hex-label" x="181" y="191">chrono</text>
    <text class="hex-label" x="123" y="205">Proposer avec</text>
    <text class="hex-label" x="123" y="214">générosité</text>
    <text class="hex-label" x="61" y="168">Avec</text>
    <text class="hex-label" x="61" y="177">efficacité</text>
    <text class="hex-label" x="61" y="90">Imaginer</text>
    <text class="hex-label" x="61" y="99">librement</text>
  </svg>
</section>

<!-- Approach -->
<section class="slide col-a row-3">
  <svg class="swoosh" viewBox="0 0 556 311" preserveAspectRatio="none" aria-hidden="true">
    <defs><linearGradient id="sw3" x1="0" y1="0" x2="1" y2="1"><stop offset="0" stop-color="#0f2f57"/><stop offset="1" stop-color="#1a4f8c"/></linearGradient></defs>
    <path d="M420 0 C520 80 560 200 470 311 L556 311 L556 0 Z" fill="url(#sw3)" opacity=".75"/>
  </svg>
  <div class="emblem" role="img" aria-label="Silhouette d'un coureur"></div>
  <div class="brand"><span class="brand-dot"></span>Lumorva</div>
  <h2 class="slide-title">1. le sprint c’est quoi ?</h2>
  <div class="section-head"><span class="chev"></span>B. Partis-pris: une approche d’expertises interconnectées</div>
  <div class="ribbons">
    <div class="ribbon">Une vision pluridisciplinaire :<br>SI, Data, Communication, Intelligence Collective, Excellence<br>opérationnelle</div>
    <div class="ribbon">Un état d’esprit et des outils<br>Design Thinking</div>
    <div class="ribbon">Une volonté farouche de présenter des solutions<br>audacieuses, réalistes et opérationnelles</div>
  </div>
</section>

<!-- Deliverables -->
<section class="slide col-b row-3">
  <svg class="swoosh" viewBox="0 0 556 311" preserveAspectRatio="none" aria-hidden="true">
    <defs><linearGradient id="sw4" x1="0" y1="0" x2="1" y2="1"><stop offset="0" stop-color="#0f2f57"/><stop offset="1" stop-color="#1a4f8c"/></linearGradient></defs>
    <path d="M420 0 C520 80 560 200 470 311 L556 311 L556 0 Z" fill="url(#sw4)" opacity=".75"/>
  </svg>
  <div class="emblem" role="img" aria-label="Silhouette d'un coureur"></div>
  <div class="brand"><span class="brand-dot"></span>Lumorva</div>
  <h2 class="slide-title">1. le sprint c’est quoi ?</h2>
  <div class="section-head"><span class="chev"></span>C/ Livrables</div>
  <ul class="deliverables">
    <li>1/ Un état des lieux</li>
    <li>2/ Mise en perspective de vos challenges digitaux stimulés par l’approche Design Thinking</li>
    <li>3/ La mise en avant des points-clés sur lesquels se déterminer pour faire évoluer votre stratégie digitale en termes de :</li>
  </ul>
</section>

</body>
</html>
```